| ▼ターゲット 10〜40代女性 健康重視な方、天然成分のサプリメントで体調管理したい方 その他6商品ほどの自社商品を出し、「お悩め解決」をテーマにしてシリーズ化を検討しております。 ▼希望デザイン方針 若くてスタイリッシュなイメージ。野菜成分仕様のため、白・緑の配色が希望 デザインイメージは添付の他社イメージを参考してください。 ▼制作依頼案 今回作っていただくのはランディングページのバナー部分となります。 今回依頼させて頂いた方にその他、同じ商品の商品紹介画像・バナー、計5〜8点のデザインをプロジェクト形式で依頼いたします。 また、今後別途依頼で別商品もお願いさせて頂く可能性があります。 ▼商品名 ブロッコリースプラウト https://www.kaimonoya-shop.jp/item/K72TQW918X/ ▼商品特徴 配合成分「ブロッコリースプラウト、明日葉、金時生姜」 スッキリする、内側からの美しさを取り入れる、自然野菜成分使用。 医薬品GMP工場で製造されたのサプリメントです。 ▼選定基準 コンセプトやイメージに沿うもの 決定後何度か修正が入る可能性がありますが、対応頂ける方。 |
皆さん素敵な提案をありがとうございました!色々迷いましたが最終的にこの提案を採用させて頂きます。理由シンプルなデザインで、弊社商品のスッキリしたイメージに適しているからです。
皆様、すばらしいご提案ありがとうございました。
今回はご縁がありませんでしたが、またの機会にお願いできればと考えております。

```html
<!DOCTYPE html>
<html lang="ja">
<head>
<meta charset="utf-8">
<title>ブロッコリースプラウト バナー</title>
<link href="https://fonts.googleapis.com/css2?family=Noto+Sans+JP:wght@400;500;700;900&display=swap" rel="stylesheet">
<style>
  :root {
    --white: #ffffff;
    --ink: #1a1a1a;
    --text: #333333;
    --green: #3f9a1f;
    --green-dark: #1f4a14;
    --green-light: #a9d57a;
    --sprout-pale: #e6f2d8;
    --badge: #5aae2a;
    --skin-soft: #f1ebe6;
  }
  html, body {
    margin: 0;
    padding: 0;
    width: 1200px;
    height: 372px;
    overflow: hidden;
    background: var(--white);
  }
  .banner {
    position: relative;
    width: 1200px;
    height: 372px;
    overflow: hidden;
    background: var(--white);
    font-family: "Noto Sans JP", sans-serif;
    color: var(--text);
  }
  .sprout-scene {
    position: absolute;
    left: 0;
    top: 0;
    width: 560px;
    height: 372px;
    background:
      radial-gradient(ellipse at 25% 80%, var(--green-light) 0%, rgba(169,213,122,0.5) 35%, rgba(230,242,216,0) 70%),
      linear-gradient(90deg, var(--sprout-pale) 0%, rgba(230,242,216,0.7) 55%, rgba(255,255,255,0) 100%);
  }
  .product-pack {
    position: absolute;
    left: 64px;
    top: 40px;
    width: 220px;
    height: 332px;
    border-radius: 14px 14px 0 0;
    background: linear-gradient(160deg, #2f6b1f 0%, var(--green-dark) 60%, #14300d 100%);
    transform: rotate(-4deg);
  }
  .tablets {
    position: absolute;
    left: 150px;
    top: 210px;
    width: 250px;
    height: 120px;
    border-radius: 60px;
    background: radial-gradient(ellipse at center, #6f7a34 0%, #4e5a22 60%, rgba(78,90,34,0) 100%);
  }
  .badge {
    position: absolute;
    left: 18px;
    top: 10px;
    width: 122px;
    height: 122px;
    border-radius: 50%;
    background: var(--badge);
    border: 4px solid var(--white);
    box-sizing: border-box;
    display: flex;
    align-items: center;
    justify-content: center;
    text-align: center;
    color: var(--white);
    font-weight: 900;
    font-size: 24px;
    line-height: 1.2;
    transform: rotate(-12deg);
  }
  .model-photo {
    position: absolute;
    right: 0;
    top: 0;
    width: 420px;
    height: 372px;
    background: linear-gradient(90deg, rgba(241,235,230,0) 0%, var(--skin-soft) 40%, #e2d8cf 100%);
  }
  .copy {
    position: absolute;
    left: 444px;
    top: 58px;
  }
  .headline {
    margin: 0;
    font-size: 50px;
    font-weight: 900;
    color: var(--ink);
    letter-spacing: 0.02em;
    line-height: 1.2;
  }
  .subline {
    margin: 14px 0 0;
    font-size: 24px;
    font-weight: 700;
    color: var(--text);
  }
  .subline .accent {
    color: var(--green);
  }
  .product-info {
    position: absolute;
    left: 446px;
    top: 248px;
  }
  .product-name {
    margin: 0;
    font-size: 24px;
    font-weight: 900;
    color: var(--ink);
  }
  .ingredients {
    margin: 8px 0 0;
    font-size: 19px;
    font-weight: 500;
    color: var(--text);
  }
  .note {
    margin: 4px 0 0;
    font-size: 15px;
    font-weight: 400;
    color: var(--text);
  }
</style>
</head>
<body>
  <div class="banner">
    <div class="sprout-scene" role="img" aria-label="ブロッコリースプラウトの若芽が広がる背景写真"></div>
    <div class="product-pack" role="img" aria-label="サプリメントの緑色のパッケージ写真"></div>
    <div class="tablets" role="img" aria-label="緑色のサプリメント錠剤の写真"></div>
    <div class="badge">お悩み<br>解決!</div>
    <div class="model-photo" role="img" aria-label="手を添えて微笑む女性の写真"></div>

    <div class="copy">
      <h1 class="headline">内側から美しく元気に!</h1>
      <p class="subline">健康が気になる方へ、<span class="accent">天然成分使用</span>のサプリメント!</p>
    </div>

    <div class="product-info">
      <p class="product-name">ブロッコリースプラウト</p>
      <p class="ingredients">配合成分:ブロッコリースプラウト・明日葉・金時生姜</p>
      <p class="note">※医薬品GMP工場で製造されたのサプリメントです。</p>
    </div>
  </div>
</body>
</html>
```